Kettle Lane Kitchen February contest

The website slider is 990 X 225 pixels to fit in with this website www.kettlelanekitchen.com.au
We would love a fun, lively, food-oriented slider created for Kettle Lane Kitchen website. Kettle Lane Kitchen is a central place where people who love food, cooking for their family and friends, and sharing recipes can hang out. We'd like the sliders to be simple, bright and to entice people to click on the link.
The banner ad needs to feature the Varnholt mixer, and to use a colour scheme that also works with the existing website. There's a blog with more information on the Varnholt mixer here http://kettlelanekitchen.com.au/uncategorized/upload-a-recipe-in-february-to-be-in-the-running-to-win-a-varnholt-mixer/
A slider in December was used to promote a similar competition which I will upload as inspiration, along with the image of the Varnholt mixer to use.
Main text: Add your best recipe by February 28 to win!
Smaller text: Best recipe as chosen by Kettle Lane Kitchen editors will win a Varnholt mixer worth $699.
Target Market(s)
Food lovers - home cooks and food bloggers. Mainly women, 30+
Industry/Entity Type
Chef

```html
<!DOCTYPE html>
<html lang="en">
<head>
<meta charset="utf-8">
<title>Kettle Lane Kitchen – February contest</title>
<link rel="stylesheet" href="https://fonts.googleapis.com/css2?family=Arimo:ital,wght@0,400;0,700;1,400&family=Lato:wght@400;700;900&family=Satisfy&display=swap">
<style>
  :root {
    --paper: #efe6d9;
    --paper-deep: #e8dccb;
    --white: #ffffff;
    --ink: #333333;
    --brown: #4a3a33;
    --orange: #d9502a;
    --red-link: #c8452a;
    --sky: #3db3d9;
    --card-base: #f7f1ea;
    --search-bg: #fdf4eb;
    --search-line: #ead9c7;
    --search-icon: #f4bf7a;
    --band-gold: #e9d49a;
  }
  * { box-sizing: border-box; margin: 0; padding: 0; }
  html, body { width: 1200px; height: 556px; overflow: hidden; background: var(--paper); }
  body { font-family: "Arimo", Arial, sans-serif; color: var(--ink); }

  .canvas { width: 1200px; height: 556px; overflow: hidden; position: relative;
    background: linear-gradient(135deg, var(--paper) 0%, var(--paper-deep) 100%); }
  .page { position: absolute; left: 0; top: 0; width: 1366px; height: 633px;
    transform: scale(0.87848); transform-origin: 0 0; }
  .abs { position: absolute; }

  /* header */
  .brand-disc { left: 181px; top: -13px; width: 178px; height: 178px; border-radius: 50%;
    background: var(--white); border: 4px solid var(--brown); z-index: 5;
    display: flex; align-items: center; justify-content: center; text-align: center; }
  .brand-name { font-weight: 700; font-size: 25px; line-height: 1.1; color: var(--brown); width: 120px; }

  .tagline { left: 517px; top: 32px; font-family: "Satisfy", cursive; font-size: 29px; color: var(--brown); white-space: nowrap; }
  .tagline-arrow { left: 868px; top: 38px; }

  .account { left: 1050px; top: 0; width: 121px; height: 30px; background: var(--white);
    border-radius: 0 0 4px 4px; font-size: 12px; display: flex; gap: 14px;
    justify-content: center; align-items: center; }
  .account a { color: var(--red-link); text-decoration: none; }

  .nav-main { left: 366px; top: 101px; width: 304px; height: 38px; background: var(--white);
    border-radius: 4px 0 0 0; display: flex; align-items: center; font-size: 12.5px; }
  .nav-main span { display: flex; align-items: center; gap: 4px; position: absolute; }
  .nav-extra { left: 670px; top: 101px; width: 501px; height: 38px; background: var(--orange);
    border-radius: 0 6px 0 0; display: flex; align-items: center; padding-left: 33px;
    color: var(--white); font-size: 12.5px; font-weight: 700; }
  .nav-extra .dot { display: inline-block; width: 5px; height: 5px; border-radius: 50%;
    background: var(--white); margin: 0 10px; }

  /* slider */
  .slider { left: 181px; top: 139px; width: 990px; height: 233px; overflow: hidden;
    border-bottom: 3px solid var(--band-gold); }
  .food-strip { position: absolute; left: 0; width: 990px; display: flex; }
  .food-strip div { flex: 1; }
  .food-strip.top { top: 0; height: 82px; }
  .food-strip.bottom { top: 151px; height: 80px; }
  .headline-band { position: absolute; left: 0; top: 82px; width: 990px; height: 69px; background: var(--white); }
  .headline { position: absolute; left: 19px; top: 91px; z-index: 2; font-family: "Lato", sans-serif;
    font-size: 28.5px; color: var(--sky); white-space: nowrap; }
  .subline { position: absolute; left: 20px; top: 124px; z-index: 2; font-family: "Lato", sans-serif;
    font-weight: 900; font-size: 12.9px; color: #1f1f1f; white-space: nowrap; }
  .mixer-shot { position: absolute; left: 752px; top: 20px; width: 232px; height: 202px; z-index: 1;
    border-radius: 30px 30px 12px 12px;
    background: linear-gradient(170deg, #dfe2e5 0%, #47b8d6 30%, #3aa8c8 60%, #c8ccd0 85%, #9ea4aa 100%); }

  /* content */
  .content { left: 181px; top: 372px; width: 990px; height: 261px; background: var(--white); }
  .section-title { display: flex; align-items: center; gap: 10px; font-size: 20px; color: var(--ink); white-space: nowrap; }

  .card { width: 200px; height: 200px; background: var(--card-base); }
  .card-photo { height: 135px; }
  .card-title { padding: 13px 0 0 10px; font-size: 14px; white-space: nowrap; }
  .card-by { padding: 9px 0 0 10px; font-size: 12px; color: var(--red-link); }

  .search { left: 861px; top: 385px; width: 297px; height: 38px; background: var(--search-bg);
    border: 1px solid var(--search-line); border-radius: 3px; font-style: italic;
    font-size: 14px; color: #555; padding: 11px 0 0 10px; }
  .search svg { position: absolute; right: 13px; top: 7px; }
  .search-scope { left: 1025px; top: 429px; font-size: 13px; color: #444; display: flex; gap: 10px; align-items: center; }
  .radio { display: inline-block; width: 12px; height: 12px; border-radius: 50%; border: 1px solid #999;
    background: #eee; vertical-align: -2px; margin-left: 3px; position: relative; }
  .radio.on::after { content: ""; position: absolute; left: 2.5px; top: 2.5px; width: 5px; height: 5px;
    border-radius: 50%; background: #555; }

  .rated-photo { width: 134px; height: 90px; }
  .rank { left: 861px; top: 533px; width: 20px; height: 36px; border-radius: 0 18px 18px 0;
    background: var(--white); font-size: 12px; color: #e3a05a; padding: 10px 0 0 0; text-align: left; }
  .rated-title { font-size: 13px; line-height: 20px; color: var(--ink); width: 152px; }
  .rated-by { font-size: 13px; color: var(--red-link); }
</style>
</head>
<body>
<div class="canvas">
<div class="page">

  <div class="abs brand-disc"><span class="brand-name">Kettle Lane Kitchen</span></div>
  <div class="abs tagline">Join the community now!</div>
  <svg class="abs tagline-arrow" width="50" height="28" viewBox="0 0 50 28">
    <path d="M3 24 Q26 26 44 6" fill="none" stroke="var(--orange)" stroke-width="2" stroke-linecap="round"/>
    <path d="M36 6 L45 4 L44 13" fill="none" stroke="var(--orange)" stroke-width="2" stroke-linecap="round" stroke-linejoin="round"/>
  </svg>
  <div class="abs account"><a href="#">Register</a><a href="#">Login</a></div>

  <nav class="abs nav-main">
    <span style="left:23px">
      <svg width="22" height="16" viewBox="0 0 22 16"><path d="M1 7 H19 Q18 15 10 15 Q2 15 1 7Z" fill="var(--orange)"/><path d="M12 6 L20 1" stroke="var(--orange)" stroke-width="2" stroke-linecap="round"/></svg>
      Recipes</span>
    <span style="left:114px">
      <svg width="20" height="18" viewBox="0 0 20 18"><circle cx="6" cy="6" r="5" fill="var(--orange)"/><circle cx="14" cy="6" r="5" fill="var(--orange)"/><rect x="4" y="7" width="12" height="10" rx="1" fill="var(--orange)"/></svg>
      Chefs</span>
    <span style="left:192px">
      <svg width="20" height="18" viewBox="0 0 20 18"><circle cx="4" cy="6" r="3" fill="var(--orange)"/><circle cx="10" cy="3.5" r="3" fill="var(--orange)"/><circle cx="16" cy="6" r="3" fill="var(--orange)"/><ellipse cx="10" cy="13" rx="6" ry="4.5" fill="var(--orange)"/></svg>
      Mentors</span>
  </nav>
  <nav class="abs nav-extra">
    Upload your recipe<i class="dot"></i>Prizes<i class="dot"></i>About<i class="dot"></i>FAQs<i class="dot"></i>Contact<i class="dot"></i>Blog
  </nav>

  <section class="abs slider">
    <div class="food-strip top" role="img" aria-label="Row of close-up food photographs: rice dishes, prawns, salad and soup">
      <div style="background:linear-gradient(160deg,#c9552c,#e0a052 50%,#7a9a3a)"></div>
      <div style="background:linear-gradient(160deg,#b9986a,#e6c48a 50%,#c45b34)"></div>
      <div style="background:linear-gradient(160deg,#d8d1c0,#4f7a35 50%,#2f2a26)"></div>
      <div style="background:linear-gradient(160deg,#2f6e7d,#d2a26a 50%,#e6c27a)"></div>
      <div style="background:linear-gradient(160deg,#d9a85a,#efd49a)"></div>
    </div>
    <div class="headline-band"></div>
    <div class="food-strip bottom" role="img" aria-label="Row of close-up food photographs: rice, pasta, tomatoes and pastry">
      <div style="background:linear-gradient(160deg,#dba25c,#e9bc78 50%,#c9873f)"></div>
      <div style="background:linear-gradient(160deg,#c9b06e,#e3cb86 50%,#8d6a3c)"></div>
      <div style="background:linear-gradient(160deg,#b8342a,#e7e1d4 50%,#c73b2c)"></div>
      <div style="background:linear-gradient(160deg,#a8732e,#d69a3c 50%,#e8c47e)"></div>
      <div style="background:linear-gradient(160deg,#e7c77e,#f1d9a2)"></div>
    </div>
    <div class="mixer-shot" role="img" aria-label="Turquoise and silver Varnholt stand mixer with steel bowl"></div>
    <div class="headline">ADD YOUR BEST RECIPE BY FEBRUARY 28 TO WIN!</div>
    <div class="subline">BEST RECIPE AS CHOSEN BY KETTLE LANE KITCHEN EDITORS WILL WIN A VARNHOLT MIXER WORTH $699.</div>
  </section>

  <main class="abs content"></main>

  <h2 class="abs section-title" style="left:193px;top:395px;font-weight:400">
    <svg width="21" height="18" viewBox="0 0 22 18"><path d="M1 8 H19 Q18 17 10 17 Q2 17 1 8Z" fill="var(--orange)"/><path d="M12 7 L20 1" stroke="var(--orange)" stroke-width="2" stroke-linecap="round"/></svg>
    Featured Recipes</h2>

  <article class="abs card" style="left:191px;top:439px">
    <div class="card-photo" role="img" aria-label="Plated open lasagne with chicken cacciatore and tomato sauce" style="background:radial-gradient(ellipse at 50% 55%,#c9773c 0%,#e9e4da 45%,#2f4a2e 80%)"></div>
    <div class="card-title">Open Cacciatore Lasagne</div>
    <div class="card-by">By Marla Penhallow</div>
  </article>
  <article class="abs card" style="left:411px;top:439px">
    <div class="card-photo" role="img" aria-label="Bowl of spaghetti bolognese topped with grated cheese" style="background:radial-gradient(ellipse at 50% 50%,#8a3a1e 0%,#c79a55 30%,#f2efe9 55%,#6a3a2a 85%)"></div>
    <div class="card-title">Spaghetti Bologanise</div>
    <div class="card-by">By Greta Ashdown</div>
  </article>
  <article class="abs card" style="left:631px;top:439px">
    <div class="card-photo" role="img" aria-label="White bowl of clear vegetable stock with potato and greens" style="background:radial-gradient(ellipse at 50% 60%,#8c8a3a 0%,#b5a25a 35%,#eeeeea 60%,#c9c5bd 90%)"></div>
    <div class="card-title">Clean Eating Vegetable Stock</div>
    <div class="card-by">By Nora Kestrel</div>
  </article>

  <div class="abs search">search
    <svg width="24" height="24" viewBox="0 0 24 24"><circle cx="10" cy="10" r="7" fill="none" stroke="var(--search-icon)" stroke-width="3"/><path d="M15 15 L22 22" stroke="var(--search-icon)" stroke-width="3.5" stroke-linecap="round"/></svg>
  </div>
  <div class="abs search-scope"><span>Recipes<i class="radio on"></i></span><span>Chefs<i class="radio"></i></span></div>

  <h2 class="abs section-title" style="left:862px;top:464px;font-weight:400">
    <svg width="21" height="18" viewBox="0 0 22 18"><path d="M1 8 H19 Q18 17 10 17 Q2 17 1 8Z" fill="var(--orange)"/><path d="M12 7 L20 1" stroke="var(--orange)" stroke-width="2" stroke-linecap="round"/></svg>
    Highest Rated Recipes</h2>

  <div class="abs rated-photo" style="left:861px;top:508px;background:linear-gradient(160deg,#6a4a2a,#f2ead8 45%,#d2a85a 75%,#c63a2a)" role="img" aria-label="White chocolate parfait with lemon curd and strawberries"></div>
  <div class="abs rank">1</div>
  <div class="abs rated-title" style="left:1005px;top:508px">White Chocolate Parfait W/ Lemon Curd and Short ..</div>
  <div class="abs rated-by" style="left:1005px;top:571px">By Ivan Marrowby</div>

  <div class="abs rated-photo" style="left:861px;top:618px;background:linear-gradient(160deg,#4a5560,#c9ccd0)" role="img" aria-label="Hot cross buns"></div>
  <div class="abs rated-title" style="left:1005px;top:618px">Hot Cross Buns</div>

</div>
</div>
</body>
</html>
```